Website design for dressage horse training business

Looking to develop a new website design for a dressage horse training website. We want to change from a single landing page to one with multiple pages.
You are free to use your creativity to design the main landing page. This is the only page you need to design at this point. I would encourage looking at other Dressage Training websites to get a feel for what is typically on them. A few websites are listed below although I think the design of them could be better.
Notes:
- Menu to include: Home, Services, News Room, Blog, About Us, Contact,
- FAQ section on main page
- Logo to remain the same - the logo attached is not the correct color so change to match existing color.
- Change 'Sponsors' to 'Partnerships' on main page
Here is the link to the current site:
https://lindenridgestables.com/
Example sites
https://www.crestwoodsporthorsesco.com/
https://corinnalavelledressage.com/
Target Market(s)
Older women with disposable income
Number of Pages Required
1 page
Look and feel
Each slider illustrates characteristics of the customer's brand and the style your logo design should communicate.

```html
<!DOCTYPE html>
<html lang="en">
<head>
<meta charset="utf-8">
<title>Linden Ridge Farm — Dressage &amp; Sport Horse Training</title>
<link href="https://fonts.googleapis.com/css2?family=Pathway+Gothic+One&family=Raleway:wght@400;500&family=Arimo:wght@400&display=swap" rel="stylesheet">
<style>
:root{
  --teal:#52a2a4;
  --brown:#6a4a3f;
  --ink:#333;
  --muted:#8a8a8a;
  --line:#e4e4e4;
  --white:#fff;
}
*{margin:0;padding:0;box-sizing:border-box}
html,body{width:1200px;height:5381px;overflow:hidden;background:var(--white)}
body{position:relative;font-family:"Raleway",sans-serif;color:var(--ink)}
.abs{position:absolute}
.heading{font-family:"Pathway Gothic One",sans-serif;font-weight:400}
.section-title{left:0;width:1200px;text-align:center;font-size:40px;color:var(--brown);line-height:1}
.dots{left:0;width:1200px;display:flex;justify-content:center;gap:4px}
.dots i{width:11px;height:11px;border:1.5px solid #bbb;border-radius:50%;display:block}
.dots.light i{border-color:rgba(255,255,255,.7)}
.btn{display:flex;align-items:center;justify-content:center;font-family:"Pathway Gothic One",sans-serif;font-size:19px;color:var(--white);box-shadow:0 2px 4px rgba(0,0,0,.25)}
.btn.brown{background:var(--brown)}
.btn.teal{background:var(--teal)}
.body-text{font-size:14.5px;line-height:31px;color:var(--muted)}

/* header */
.top-info{top:43px;font-family:"Arimo",sans-serif;font-size:20px;color:#444;display:flex;align-items:center;gap:6px}
.brand{top:32px;left:0;width:1200px;text-align:center;font-size:44px;color:var(--brown);letter-spacing:2px}
.header-rule{top:111px;left:110px;width:980px;height:1px;background:var(--line)}
.main-nav{top:128px;left:0;width:1200px;display:flex;justify-content:center;font-family:"Arimo",sans-serif;font-size:15px;color:#333}
.main-nav a{color:inherit;text-decoration:none;padding:0 27px;position:relative}
.main-nav a.active::after{content:"";position:absolute;left:27px;right:27px;bottom:-5px;height:1px;background:#333}

/* hero */
.hero{top:184px;left:0;width:1200px;height:729px;overflow:hidden;
  background:
    radial-gradient(ellipse 260px 420px at 330px 220px,rgba(120,100,80,.55),transparent 70%),
    radial-gradient(ellipse 500px 200px at 300px 680px,rgba(110,90,70,.45),transparent 70%),
    linear-gradient(90deg,#2f2a25 0%,#3e362e 45%,#2c2925 100%)}
.hero-circle{left:507px;top:42px;width:626px;height:626px;border-radius:50%;border:7px solid var(--teal);overflow:hidden;
  background:
    radial-gradient(ellipse 150px 260px at 72% 42%,#4a2e1e 0%,#5c3a26 55%,transparent 80%),
    radial-gradient(ellipse 90px 170px at 33% 48%,#5f82b0 0%,#7a8fa8 50%,transparent 80%),
    linear-gradient(180deg,#c9c6b6 0%,#b2a888 30%,#a08760 55%,#9c7e58 75%,#8a6d4a 100%)}
.socials{left:38px;top:209px;display:flex;gap:14px}
.socials span{width:18px;height:18px;background:var(--white);border-radius:2px;display:block}
.hero-title{left:38px;top:252px;font-size:35px;line-height:44px;color:var(--white)}
.hero-sub{left:38px;top:358px;font-size:22px;color:var(--white)}

/* cards */
.card{left:111px;width:978px;height:310px;background:var(--white);box-shadow:0 0 6px rgba(0,0,0,.18)}
.card-title{font-size:25px;color:var(--teal)}
.card-text{font-size:14.5px;line-height:31px;color:var(--muted)}

/* about */
.about-col{top:1850px;height:560px;width:400px}
.about-text{color:var(--white);font-size:12.5px;line-height:30.5px;text-align:center}

/* partnerships */
.partner-title{font-size:31px;color:var(--teal)}
.partner-name{font-size:38px;text-align:center}

/* faq */
.faq-item{left:598px;width:481px;height:58px;border:1px solid var(--line);box-shadow:0 1px 4px rgba(0,0,0,.1);font-family:"Arimo",sans-serif;font-size:14px;color:#333;padding:20px 0 0 10px}
.faq-item .toggle{position:absolute;right:12px;top:14px;font-size:22px;line-height:1}
.faq-item p{font-family:"Raleway",sans-serif;font-size:12px;line-height:23px;color:#aaa;margin-top:14px;padding-right:20px}

/* contact */
.contact-line{left:400px;width:400px;text-align:center;color:var(--white);font-family:"Arimo",sans-serif;font-size:17px;display:flex;justify-content:center;align-items:center;gap:6px}
</style>
</head>
<body>

<header>
  <div class="abs top-info" style="left:110px">
    <svg width="13" height="19" viewBox="0 0 12 18" aria-hidden="true"><path d="M6 0C2.7 0 0 2.7 0 6c0 4.5 6 12 6 12s6-7.5 6-12c0-3.3-2.7-6-6-6zm0 8.5A2.5 2.5 0 1 1 6 3.5a2.5 2.5 0 0 1 0 5z" fill="#52a2a4"/></svg>
    Iowa, USA
  </div>
  <div class="abs heading brand">LINDEN RIDGE FARM</div>
  <div class="abs top-info" style="right:112px">
    <svg width="17" height="17" viewBox="0 0 24 24" aria-hidden="true"><path d="M6.6 10.8a15.1 15.1 0 0 0 6.6 6.6l2.2-2.2a1 1 0 0 1 1-.25 11.4 11.4 0 0 0 3.6.57 1 1 0 0 1 1 1V20a1 1 0 0 1-1 1A17 17 0 0 1 3 4a1 1 0 0 1 1-1h3.5a1 1 0 0 1 1 1c0 1.25.2 2.45.57 3.6a1 1 0 0 1-.25 1z" fill="#52a2a4"/></svg>
    515-555-0182
  </div>
  <div class="abs header-rule"></div>
  <nav class="abs main-nav">
    <a class="active" href="#">Home</a><a href="#">Services</a><a href="#">News Room</a><a href="#">Blog</a><a href="#">About Us</a><a href="#">Contact</a>
  </nav>
</header>

<section class="abs hero" role="img" aria-label="Dimmed photo of a rider schooling a horse in an arena">
  <div class="abs hero-circle" role="img" aria-label="Photo of a trainer in a plaid shirt working a rearing bay horse along a wooden fence"></div>
  <div class="abs socials" aria-label="Social links"><span></span><span></span><span></span></div>
  <h1 class="abs heading hero-title">Central Iowa's Premier dressage and<br>sport horse training</h1>
  <p class="abs heading hero-sub">Located outside Des Moines, Iowa</p>
  <a class="abs btn teal" style="left:38px;top:420px;width:154px;height:50px">Services</a>
  <a class="abs btn brown" style="left:200px;top:420px;width:155px;height:50px">Contact</a>
</section>

<h2 class="abs heading section-title" style="top:1013px">Training &amp; Lessons</h2>
<div class="abs dots" style="top:1072px"><i></i><i></i><i></i></div>

<article class="abs card" style="top:1112px">
  <h3 class="abs heading card-title" style="left:44px;top:50px">Training</h3>
  <p class="abs card-text" style="left:44px;top:93px;width:500px;text-align:justify">Linden Ridge Farm offers both full and half time training options with Hannah Corliss. There is much flexibility with both rides and/or lessons weekly in the training packages..</p>
  <a class="abs btn brown" style="left:46px;top:207px;width:154px;height:48px">Know More</a>
  <div class="abs" style="left:604px;top:6px;width:368px;height:298px;background:
    radial-gradient(ellipse 40px 70px at 36% 58%,#4a2e20,transparent 80%),
    radial-gradient(ellipse 500px 180px at 50% 0%,#f2f1ec 0%,#d9d6cc 60%,transparent 100%),
    linear-gradient(180deg,#e6e3da 0%,#c7bfae 48%,#a87a52 62%,#8f6240 100%)" role="img" aria-label="Photo of a rider on a bay horse in a covered arena with a trainer on the ground"></div>
</article>

<article class="abs card" style="top:1438px">
  <div class="abs" style="left:6px;top:6px;width:366px;height:298px;background:
    radial-gradient(ellipse 70px 110px at 58% 42%,#d8d4cc,transparent 80%),
    radial-gradient(ellipse 120px 110px at 52% 78%,#1f1a18,transparent 85%),
    linear-gradient(160deg,#5c4636 0%,#9c7d5e 35%,#6a5340 60%,#b08e6a 100%)" role="img" aria-label="Photo of a rider on a dark horse in an indoor arena"></div>
  <h3 class="abs heading card-title" style="left:422px;top:50px;color:var(--brown)">Lessons</h3>
  <p class="abs card-text" style="left:422px;top:93px;width:510px">Lessons are available for all ages of riders. Hannah thoroughly enjoys working with accomplished riders looking to succeed in the show ring, as well as riders</p>
  <a class="abs btn teal" style="left:422px;top:205px;width:155px;height:50px">Read More</a>
</article>

<section>
  <div class="abs about-col" style="left:0;background:
    radial-gradient(ellipse 150px 260px at 32% 55%,#8e4f2c,transparent 85%),
    radial-gradient(ellipse 110px 200px at 78% 72%,#2e3236,transparent 85%),
    linear-gradient(180deg,#c8c6c2 0%,#b7aa96 50%,#7a6a50 100%)" role="img" aria-label="Photo of a rider kissing a chestnut horse on the nose"></div>
  <div class="abs about-col" style="left:400px;background:var(--teal)">
    <h2 class="abs heading" style="left:0;width:400px;top:50px;text-align:center;font-size:40px;color:var(--white)">About Us</h2>
    <div class="abs dots light" style="width:400px;top:110px"><i></i><i></i><i></i></div>
    <p class="abs about-text" style="left:20px;top:150px;width:360px">FEI rider and trainer, Hannah Corliss began her riding career at a young age. She went up through the ranks of Pony Club and with an emphasis and focus in eventing. During college, Hannah worked for a small breeder starting young horses. Hannah loves starting young horses including starting and guiding them in a correct and quiet way to help them flourish. Her training focuses on gymnastic training incorporating ground work/lunging/long lining.</p>
    <a class="abs btn brown" style="left:123px;top:455px;width:154px;height:49px">Read More</a>
  </div>
  <div class="abs about-col" style="left:800px;background:
    radial-gradient(ellipse 90px 80px at 70% 12%,#e8e6e2,transparent 85%),
    radial-gradient(ellipse 200px 170px at 45% 35%,#3a2a24,transparent 85%),
    linear-gradient(180deg,#5a4638 0%,#8a7a6c 45%,#c2bcb4 75%,#d2ccc4 100%)" role="img" aria-label="Photo of a rider in white breeches on a bay horse in an arena"></div>
</section>

<h2 class="abs heading section-title" style="top:2509px">Partnerships</h2>
<div class="abs dots" style="top:2568px"><i></i><i></i><i></i></div>

<h3 class="abs heading partner-title" style="left:111px;top:2634px">Fieldstone Saddlery</h3>
<p class="abs body-text" style="left:111px;top:2692px;width:572px;text-align:justify">Fieldstone Saddlery is constantly designing and researching saddles and riders to find the right blend of design and craftsmanship to fit today's demands. Every saddle's detail is carefully checked to be sure the workmanship and quality is there. All saddles are anatomically designed for horse and rider, hand-crafted from the finest leathers, and manufactured using the most technically advanced methods and features available.</p>
<a class="abs btn brown" style="left:111px;top:2903px;width:154px;height:50px">Read More</a>
<div class="abs heading partner-name" style="left:736px;top:2752px;width:336px;color:var(--brown)">Fieldstone Saddlery</div>

<h3 class="abs heading partner-title" style="right:111px;top:2985px">Whitfield's Saddlery</h3>
<div class="abs heading partner-name" style="left:150px;top:3105px;width:280px;color:#1f3a2c">Whitfield's Saddlery</div>
<p class="abs body-text" style="left:504px;top:3043px;width:576px;text-align:justify;text-align-last:right">My goal is to provide the best possible fit for both horse and rider whether it is a saddle you already own, one you have on trial, or one that I carry. Being a Qualified Saddle Fitter by the Saddle Fitters Association allows me to work with all saddle types and brands. In addition, I carry a broad range of saddles to fit your needs, both new and used. Having a multitude of saddles in my stock makes saddle shopping much easier for you</p>
<a class="abs btn brown" style="left:934px;top:3252px;width:155px;height:52px">Know More</a>

<section class="abs" style="left:0;top:3409px;width:1200px;height:529px;background:
    radial-gradient(ellipse 330px 200px at 800px 240px,rgba(140,80,40,.6),transparent 80%),
    radial-gradient(ellipse 90px 220px at 200px 260px,rgba(90,120,120,.45),transparent 85%),
    linear-gradient(180deg,#3d3c40 0%,#47433f 40%,#3a3a2c 75%,#2e3326 100%)" role="img" aria-label="Dimmed photo of a handler standing with a chestnut horse in a field">
  <h2 class="abs heading" style="left:0;width:1200px;top:81px;text-align:center;font-size:40px;color:var(--white)">For Sale</h2>
  <div class="abs dots light" style="top:139px"><i></i><i></i><i></i></div>
  <h3 class="abs heading" style="left:0;width:1200px;top:208px;text-align:center;font-size:31px;color:var(--teal)">Aurelian Crest</h3>
  <p class="abs" style="left:118px;top:259px;width:964px;text-align:center;color:var(--white);font-size:14.5px;line-height:30.5px">Aurelian Crest, "Remy," (Caspian x Northern Valor) is a 2012, 16hh imported Hanoverian. Remy is an incredibly quiet and kind horse. He is ridden by both an amateur and child rider. He loves to hack and is very quiet alone and with a group of horses. He has shown through first level with scores into the 70's at both training and first level. Remy is currently solidly schooling all of second level, as well as half passes and flying changes from third level. Remy has 3 very easy to ride gaits and it is easy for riders to sit his trot. Very quiet and well mannered on the ground with vet, farrier and clipping. He has lovely confirmation with a striking head. He is regularly admired at shows! Remy is very versatile and game and also loves to jump!</p>
</section>

<h2 class="abs heading section-title" style="top:4037px">FAQ</h2>
<div class="abs dots" style="top:4096px"><i></i><i></i><i></i></div>
<div class="abs" style="left:111px;top:4166px;width:464px;height:558px;background:
    radial-gradient(ellipse 120px 200px at 34% 45%,#c6c8ce,transparent 85%),
    radial-gradient(ellipse 140px 180px at 72% 30%,#6e3a20,transparent 85%),
    linear-gradient(180deg,#d8d4ca 0%,#a48466 40%,#7a8a5a 70%,#4e6e2e 100%)" role="img" aria-label="Photo of a rider in a cap and hoodie leading a bay horse on grass"></div>

<div class="abs faq-item" style="top:4189px">Lorem ipsum dolor sit amet, consectetur adipiscing elit<span class="toggle">+</span></div>
<div class="abs faq-item" style="top:4268px">Lorem ipsum dolor sit amet, consectetur adipiscing elit<span class="toggle">+</span></div>
<div class="abs faq-item" style="top:4347px">Lorem ipsum dolor sit amet, consectetur adipiscing elit<span class="toggle">+</span></div>
<div class="abs faq-item" style="top:4427px">Lorem ipsum dolor sit amet, consectetur adipiscing elit<span class="toggle">+</span></div>
<div class="abs faq-item" style="top:4506px;height:117px">Lorem ipsum dolor sit amet, consectetur adipiscing elit<span class="toggle">-</span><p>Sed ut perspiciatis unde omnis iste natus error sit voluptatem accusantium doloremque laudantium, totam rem aperiam, eaque ipsa</p></div>
<div class="abs faq-item" style="top:4636px">Lorem ipsum dolor sit amet, consectetur adipiscing elit<span class="toggle">+</span></div>

<section>
  <div class="abs" style="left:0;top:4824px;width:400px;height:557px;background:
    radial-gradient(ellipse 60px 120px at 70% 30%,#d4e6d0,transparent 85%),
    radial-gradient(ellipse 80px 60px at 20% 75%,#dfe9d8,transparent 85%),
    linear-gradient(135deg,#eef0f2 0%,#e2e7ea 50%,#e9ebe4 100%)" role="img" aria-label="Street map of the Des Moines area"></div>
  <div class="abs" style="left:400px;top:4824px;width:400px;height:557px;background:var(--brown)">
    <h2 class="abs heading" style="left:0;width:400px;top:52px;text-align:center;font-size:40px;color:var(--white)">Contact Me</h2>
    <div class="abs dots light" style="width:400px;top:111px"><i></i><i></i><i></i></div>
    <p class="abs" style="left:30px;width:340px;top:155px;text-align:center;color:var(--white);font-size:12.5px;line-height:31px">If you are interested in learning more about Linden Ridge Farm's services or availability for training or lessons, please contact us below!</p>
  </div>
  <div class="abs contact-line" style="top:5095px">
    <svg width="16" height="16" viewBox="0 0 24 24" aria-hidden="true"><rect width="24" height="24" rx="3" fill="#fff"/><path d="M7.5 11a10 10 0 0 0 5.5 5.5l1.6-1.6a.8.8 0 0 1 .8-.2 8 8 0 0 0 2.6.4.8.8 0 0 1 .8.8V18a.8.8 0 0 1-.8.8A12.8 12.8 0 0 1 5.2 6a.8.8 0 0 1 .8-.8h2.1a.8.8 0 0 1 .8.8 8 8 0 0 0 .4 2.6.8.8 0 0 1-.2.8z" fill="#6a4a3f"/></svg>
    Telephone - &nbsp;515-555-0182
  </div>
  <div class="abs contact-line" style="top:5137px">
    <svg width="16" height="16" viewBox="0 0 24 24" aria-hidden="true"><rect width="24" height="24" rx="3" fill="#fff"/><path d="M7.5 11a10 10 0 0 0 5.5 5.5l1.6-1.6a.8.8 0 0 1 .8-.2 8 8 0 0 0 2.6.4.8.8 0 0 1 .8.8V18a.8.8 0 0 1-.8.8A12.8 12.8 0 0 1 5.2 6a.8.8 0 0 1 .8-.8h2.1a.8.8 0 0 1 .8.8 8 8 0 0 0 .4 2.6.8.8 0 0 1-.2.8z" fill="#6a4a3f"/></svg>
    info@lindenridgestables.com
  </div>
  <div class="abs contact-line" style="top:5338px;font-size:14px">© 2021 All Rights Reserved</div>
  <div class="abs" style="left:800px;top:4824px;width:400px;height:557px;background:
    radial-gradient(ellipse 160px 260px at 75% 25%,#5a2e1c,transparent 85%),
    radial-gradient(ellipse 80px 200px at 25% 30%,#f2f2f0,transparent 85%),
    linear-gradient(180deg,#4a2e22 0%,#8a5a40 35%,#c8b8a0 65%,#a89072 100%)" role="img" aria-label="Photo of a horse's legs in boots jumping a white fence"></div>
</section>

</body>
</html>
```